Peanut Butter for Dogs - Label

Dear Designers,

Our company develops natural & innovative products aimed at enhancing animal (cat & dog) well-being. The company focuses on producing high-end, ethically sourced products that naturally soothe pets, improving their quality of life.

We are currently developing a new CBD-enriched Peanut Butter product for dogs, and we are looking for some label designs that follow our brand image & brand identity.

-> Please see full brief PDF file attached.

Target Market(s)

European Market (French Speaking)

Industry/Entity Type

Pet Food

Font styles to use
Other font styles liked:
• Please see brand kit in PDF brief

Colors

Designer to choose colors to be used in the design.

Requirements
Must have
• Please see brief PDF file attached
Nice to have
Should not have

```html
<!DOCTYPE html>
<html lang="fr">
<head>
<meta charset="utf-8">
<title>Douceur Réconfortante – Étiquette</title>
<link rel="stylesheet" href="https://fonts.googleapis.com/css2?family=Anton&family=Montserrat:wght@400;500;600;700;800&family=Quicksand:wght@500&display=swap">
<style>
  :root {
    --pink: #e7b2bd;
    --pink-light: #efc2cb;
    --green: #399a7c;
    --green-dark: #2f8369;
    --ink: #333333;
    --dark-box: #2e2e2e;
    --white: #ffffff;
    --nut-light: #f3d9a6;
    --nut-mid: #e2b16e;
    --nut-dark: #c98a45;
  }
  * { box-sizing: border-box; margin: 0; padding: 0; }
  html, body { width: 1200px; height: 1000px; overflow: hidden; background: #ffffff; }
  body { position: relative; font-family: "Montserrat", sans-serif; }

  .label {
    position: absolute; left: 20px; top: 278px;
    width: 1160px; height: 444px; overflow: hidden;
  }
  .label__background { position: absolute; inset: 0; width: 100%; height: 100%; }

  /* back panel */
  .panel-back {
    position: absolute; left: 21px; top: 38px; width: 264px;
    color: var(--ink); font-size: 11.3px; line-height: 1.27;
  }
  .panel-back p { text-align: justify; margin-bottom: 11px; }
  .panel-back strong { font-weight: 700; }
  .panel-back .tagline { font-weight: 600; margin: 0 0 8px 2px; }
  .trademark { color: var(--white); }
  .dosage-title { font-weight: 700; margin: 15px 0 4px; }
  .dosage-list { list-style: none; width: 153px; margin-bottom: 12px; }
  .dosage-list li {
    padding: 4px 0 5px; border-bottom: 1px solid rgba(51,51,51,0.35);
  }
  .dosage-list li:last-child { border-bottom: 1px solid rgba(51,51,51,0.35); }
  .net-weight { color: var(--white); font-weight: 700; margin-top: 18px; }

  /* front panel */
  .panel-front { position: absolute; left: 307px; top: 0; width: 546px; height: 444px; }
  .brand-name {
    position: absolute; top: 80px; left: 0; width: 100%; text-align: center;
    font-weight: 500; font-size: 32px; letter-spacing: 1px; color: var(--white);
  }
  .tag-box {
    position: absolute; background: var(--dark-box); color: var(--white);
    font-weight: 800; text-align: center; white-space: nowrap;
  }
  .tag-box--cbd { left: 175px; top: 171px; width: 197px; height: 44px; font-size: 27px; line-height: 44px; }
  .product-title {
    position: absolute; top: 196px; left: 0; width: 100%; text-align: center;
    font-family: "Anton", sans-serif; font-size: 150px; line-height: 1;
    letter-spacing: 2px; color: var(--white);
  }
  .product-photo {
    position: absolute; left: 0; bottom: 0; width: 100%; height: 95px;
    background: linear-gradient(180deg, var(--nut-mid), var(--nut-light) 45%, var(--nut-dark));
  }
  .tag-box--sub { left: 140px; top: 336px; width: 267px; height: 41px; font-size: 24px; line-height: 41px; }
  .flavour {
    position: absolute; left: 192px; top: 372px; width: 163px; height: 20px;
    background: var(--green); color: var(--ink); font-size: 12.5px; font-weight: 500;
    text-align: center; line-height: 20px;
  }
  .floating-nut {
    position: absolute; border-radius: 50%;
    background: radial-gradient(circle at 40% 35%, var(--nut-light), var(--nut-mid));
  }

  /* side panel */
  .panel-side { position: absolute; left: 853px; top: 0; width: 307px; height: 444px; }
  .badge {
    position: absolute; top: 294px; width: 48px; height: 48px; border-radius: 50%;
    border: 3px solid var(--white);
  }
  .benefits {
    position: absolute; left: 28px; top: 364px; list-style: none;
    font-family: "Quicksand", sans-serif; font-size: 16px; line-height: 19px; color: var(--white);
  }
  .benefits li::before { content: "• "; }
</style>
</head>
<body>
<div class="label">
  <svg class="label__background" viewBox="0 0 1160 444" preserveAspectRatio="none" aria-hidden="true">
    <rect width="1160" height="444" fill="var(--pink)"/>
    <rect x="307" width="546" height="200" fill="var(--pink-light)" opacity="0.35"/>
    <path d="M0 165 L307 165 L307 187 Q580 198 853 187 L1160 165 L1160 444 L0 444 Z" fill="var(--green)"/>
  </svg>

  <section class="panel-back">
    <p class="tagline">Doux comme une caresse</p>
    <p>Enrichi en extrait de chanvre naturellement apaisant, le beurre de cacahuète <span class="trademark">NUTIPAWTM</span> est une délicieuse friandise d’occupation à lécher.</p>
    <p><strong>Utilisation :</strong> Laissez votre chien lécher cette gourmandise pour traverser en douceur les événements stressants du quotidien (absence, toilettage, trajet en voiture, etc.)</p>
    <p style="text-align:left"><strong>Astuce :</strong> Pour une utilisation optimale, étalez le beurre de cacahuète<br>sur le tapis de léchage <span class="trademark">LICKIPAWTM</span>.</p>
    <div class="dosage-title">Dosage table:</div>
    <ul class="dosage-list">
      <li>Petit : 1 cuillère à café</li>
      <li>Moyen : 2 cuillères à café</li>
      <li>Grand : 3 cuillères à café</li>
    </ul>
    <p style="text-align:left"><strong>Ingrédients :</strong> Beurre de cacahuète, extrait de chanvre (0% THC).</p>
    <div class="net-weight">Poids Net : 250g</div>
  </section>

  <section class="panel-front">
    <div class="floating-nut" role="img" aria-label="Cacahuète décortiquée" style="left:12px;top:28px;width:70px;height:46px;transform:rotate(35deg)"></div>
    <div class="floating-nut" role="img" aria-label="Cacahuète décortiquée" style="left:55px;top:127px;width:72px;height:30px;transform:rotate(15deg)"></div>
    <div class="floating-nut" role="img" aria-label="Cacahuète décortiquée" style="left:404px;top:110px;width:46px;height:26px;transform:rotate(-50deg)"></div>
    <div class="floating-nut" role="img" aria-label="Cacahuète décortiquée" style="left:475px;top:50px;width:78px;height:40px;transform:rotate(-70deg)"></div>
    <div class="brand-name">VERDALIA</div>
    <div class="product-photo" role="img" aria-label="Cacahuètes et beurre de cacahuète"></div>
    <div class="tag-box tag-box--cbd">CBD 150 MG</div>
    <h1 class="product-title">DOUCEUR</h1>
    <div class="tag-box tag-box--sub">RECONFORTANTE</div>
    <div class="flavour">BEURRE DE CACAHUÈTE</div>
  </section>

  <section class="panel-side">
    <div class="badge" style="left:32px"></div>
    <div class="badge" style="left:105px"></div>
    <div class="badge" style="left:178px"></div>
    <ul class="benefits">
      <li>Anti-Stress</li>
      <li>100% naturel</li>
      <li>A lécher</li>
    </ul>
  </section>
</div>
</body>
</html>
```